Brighten Your Calling - book web site

I need a web site for my book that is being published and will be available on Tellurio April 6th. It will have an email opt in which will then email the person a pdf report.
And it will have a bio page.
My logo, pic, book cover and bio details are attached below.

Target Market(s)

New life coaches that are looking to figure out their purpose and branding for their business

Industry/Entity Type

Life Coaching

Number of Pages Required

3 page

Font styles to use
Serif

Requirements
Must have
• The book cover, my logo, an opt in page, a bio page, my picture
• i would like the book in the header
• Needs to be chatterloop compliant
Should not have
• except for the logo, willow heart and soul will NOT be highlighted in the header

```html
<!DOCTYPE html>
<html lang="en">
<head>
<meta charset="utf-8">
<title>Brighten Your Calling – Maren Holloway</title>
<link rel="stylesheet" href="https://fonts.googleapis.com/css2?family=Crimson+Pro:wght@400&family=Open+Sans:wght@400;600&family=Nunito+Sans:wght@400;600&display=swap">
<style>
  :root {
    --title-red: #8e1b1f;
    --accent-orange: #e0661d;
    --sun-yellow: #f5b400;
    --ember: #e2431f;
    --ink: #2b2b2b;
    --grey-text: #5a5a5a;
    --body-text: #666666;
    --field-border: #cfcfcf;
    --field-fill: #f7f7f7;
    --footer-red: #a30f12;
    --white: #ffffff;
  }
  * { box-sizing: border-box; margin: 0; padding: 0; }
  html, body { width: 1200px; height: 2835px; overflow: hidden; }
  body { position: relative; background: var(--white); font-family: "Open Sans", sans-serif; color: var(--ink); }
  h1, h2, h3 { font-weight: 400; }
  .abs { position: absolute; }

  /* Header / hero */
  .hero { position: absolute; left: 0; top: 0; width: 1200px; height: 690px; overflow: hidden;
    background:
      radial-gradient(ellipse 520px 300px at 900px 300px, rgba(255,255,255,.75), transparent 70%),
      radial-gradient(ellipse 400px 260px at 300px 520px, rgba(255,255,255,.6), transparent 70%),
      radial-gradient(ellipse 500px 260px at 1050px 600px, rgba(246,222,232,.7), transparent 70%),
      linear-gradient(160deg, #a9d3bd 0%, #c4e2d1 40%, #b6d9c5 70%, #e6efe9 100%); }
  .hero-curve { position: absolute; left: 0; bottom: 0; width: 1200px; height: 80px; }
  .site-name { position: absolute; font-family: "Nunito Sans", sans-serif; font-weight: 600; font-size: 24px;
    color: var(--ink); white-space: nowrap; line-height: 1; }
  .main-nav { position: absolute; left: 698px; top: 64px; display: flex; gap: 38px;
    font-family: "Nunito Sans", sans-serif; font-size: 18px; color: var(--ink); text-transform: uppercase; }
  .hero-title { position: absolute; left: 120px; top: 255px; font-family: "Crimson Pro", serif;
    font-size: 58px; line-height: 54px; color: var(--title-red); letter-spacing: .5px; }
  .hero-byline { position: absolute; left: 124px; top: 374px; font-family: "Crimson Pro", serif; font-size: 32px; color: var(--ink); }
  .store-badge { display: inline-flex; align-items: center; justify-content: center; width: 122px; height: 48px;
    background: var(--white); border: 1px solid #9a9a9a; border-radius: 7px; box-shadow: 0 2px 3px rgba(0,0,0,.25);
    font-family: "Open Sans", sans-serif; font-weight: 600; font-size: 17px; color: var(--ink); }
  .hero-buy { position: absolute; left: 132px; top: 438px; display: flex; align-items: center; gap: 12px; font-size: 14px; }
  .slider-dots { position: absolute; left: 525px; top: 589px; display: flex; gap: 10px; }
  .slider-dots span { width: 30px; height: 4px; background: var(--white); }

  /* Latest book */
  .book-kicker { left: 125px; top: 722px; font-family: "Crimson Pro", serif; font-size: 36px; color: var(--accent-orange); }
  .book-title { left: 125px; top: 764px; font-family: "Crimson Pro", serif; font-size: 35px; color: var(--grey-text); }
  .book-copy { left: 127px; top: 834px; width: 592px; font-size: 14px; line-height: 25px; color: var(--body-text); text-align: justify; }
  .book-copy p + p { margin-top: 14px; }
  .book-buy { left: 128px; top: 1066px; display: flex; align-items: center; gap: 20px; font-family: "Nunito Sans", sans-serif; font-size: 16.5px; color: var(--ink); }
  .book-cover { left: 762px; top: 712px; width: 262px; height: 390px;
    background: radial-gradient(ellipse at 50% 45%, #8fcfa9, #5fae88 60%, #3f8f6e); }

  /* About band */
  .about-band { left: 0; top: 1223px; width: 1200px; height: 538px;
    background: linear-gradient(120deg, var(--sun-yellow) 0%, #f09a0e 35%, #e8611c 70%, var(--ember) 100%); }
  .portrait { left: 129px; top: 1291px; width: 287px; height: 416px;
    background: linear-gradient(180deg, #7d7b7c 0%, #5e5556 40%, #3c3234 100%); }
  .portrait-frame { position: absolute; left: 9px; top: 9px; right: 9px; bottom: 9px; border: 1px solid rgba(255,255,255,.85); }
  .about-title { left: 459px; top: 1290px; font-family: "Crimson Pro", serif; font-size: 36px; color: var(--white); }
  .about-copy { left: 461px; top: 1358px; width: 608px; font-size: 14px; line-height: 25px; color: var(--white); }
  .about-copy p + p { margin-top: 16px; }
  .read-more { left: 461px; top: 1640px; width: 144px; height: 41px; border: 1.5px solid var(--white);
    display: flex; align-items: center; justify-content: center; font-family: "Crimson Pro", serif; font-size: 15px; color: var(--white); letter-spacing: .5px; }

  /* Email sign-up */
  .signup-band { left: 0; top: 1761px; width: 1200px; height: 341px;
    background: linear-gradient(180deg, rgba(60,50,45,.45), rgba(40,32,28,.5)),
      linear-gradient(100deg, #7a6a5a 0%, #b3946b 45%, #8c7a66 70%, #5e5048 100%); }
  .signup-title { left: 0; width: 1200px; top: 1830px; text-align: center; font-family: "Crimson Pro", serif; font-size: 36px; color: var(--white); }
  .signup-copy { left: 230px; width: 740px; top: 1880px; text-align: center; font-size: 14px; line-height: 25px; color: rgba(255,255,255,.75); }
  .signup-form { left: 308px; top: 1960px; display: flex; }
  .signup-input { width: 425px; height: 45px; background: var(--white); display: flex; align-items: center; padding-left: 24px; font-size: 15px; color: #666; }
  .signup-button { width: 152px; height: 45px; background: #dc3d1c; color: var(--white); display: flex; align-items: center; justify-content: center; font-size: 18px; }

  /* Contact */
  .contact-title { left: 0; width: 1200px; top: 2140px; text-align: center; font-family: "Crimson Pro", serif; font-size: 42px; color: var(--ink); }
  .field-label { left: 139px; font-family: "Nunito Sans", sans-serif; font-size: 16px; color: var(--grey-text); }
  .field { left: 138px; width: 440px; background: var(--field-fill); border: 1px solid var(--field-border); }
  .submit { left: 142px; top: 2534px; width: 151px; height: 46px; background: var(--sun-yellow); color: var(--white);
    display: flex; align-items: center; justify-content: center; font-weight: 600; font-size: 17px; }
  .contact-info { left: 686px; top: 2235px; font-family: "Nunito Sans", sans-serif; font-size: 16px; color: var(--grey-text); line-height: 45.5px; }
  .social { left: 686px; top: 2415px; display: flex; gap: 12px; }
  .social span { width: 38px; height: 38px; border-radius: 50%; background: var(--sun-yellow); }

  /* Footer */
  .site-footer { left: 0; top: 2680px; width: 1200px; height: 155px; background: var(--footer-red); color: var(--white); text-align: center; }
  .copyright { margin-top: 36px; font-family: "Nunito Sans", sans-serif; font-size: 17px; }
  .legal-links { margin-top: 14px; font-family: "Nunito Sans", sans-serif; font-size: 15px; }
</style>
</head>
<body>

<header class="hero" role="img" aria-label="Soft close-up of pale green and white feathers">
  <span class="site-name" style="left:104px; top:66px;">Willow Heart and Soul</span>
  <nav class="main-nav"><span>Buy My Book</span><span>About Me</span><span>Contact</span></nav>
  <h1 class="hero-title">BRIGHTEN<br>YOUR CALLING</h1>
  <p class="hero-byline">By Maren Holloway</p>
  <div class="hero-buy"><span class="store-badge">Tellurio</span><span>April 6th</span></div>
  <div class="slider-dots"><span></span><span></span><span></span><span></span></div>
  <svg class="hero-curve" viewBox="0 0 1200 80" preserveAspectRatio="none" aria-hidden="true">
    <path d="M0 65 Q600 -30 1200 65 L1200 80 L0 80 Z" fill="#ffffff"/>
  </svg>
</header>

<section aria-label="Latest book">
  <h2 class="abs book-kicker">Latest Book</h2>
  <h3 class="abs book-title">Brighten Your Calling</h3>
  <div class="abs book-copy">
    <p>Maren Holloway, founder of Willow Heart and Soul, helps new coaches and creative entrepreneurs find their inner voice so that they have the confidence to bring their authentic selves out into the world. Maren has gone through this process for herself and helped other new businesses achieve dramatic improvements in their organization and focus as a result</p>
    <p>Maren Holloway, founder of Willow Heart and Soul, helps new coaches and creative entrepreneurs find their inner voice so that they have the confidence to bring their authentic selves out into the world.</p>
  </div>
  <div class="abs book-buy"><span>Buy from Tellurio April 6th</span><span class="store-badge" style="width:142px;height:54px;">Tellurio</span></div>
  <div class="abs book-cover" role="img" aria-label="Book cover of Brighten Your Calling by Maren Holloway"></div>
</section>

<section aria-label="About the author">
  <div class="abs about-band"></div>
  <div class="abs portrait" role="img" aria-label="Portrait photograph of Maren Holloway"><span class="portrait-frame"></span></div>
  <h2 class="abs about-title">Little About Me</h2>
  <div class="abs about-copy">
    <p>Maren has helped businesses achieve dramatic improvements in their organization and focus – in turn, making their businesses more profitable. Clients who seek Maren’s guidance are ready to get real and get wise, both in terms of health and business goals.</p>
    <p>She helps coaches quickly recognize easy to integrate strategies that will suit their work style to help eliminate the confusion on what to do next which in turn will boost their confidence and their bottom line.</p>
    <p>Maren is a classically trained culinary chef from Harbor &amp; Vale Institute and a certified raw foods chef, a certified yoga instructor, reiki master, a StillWave facilitator, and a certified Business Coach for Wellness and Artistic Professionals</p>
  </div>
  <div class="abs read-more">READ MORE</div>
</section>

<section aria-label="Email sign up">
  <div class="abs signup-band" role="img" aria-label="Woman sitting in tall grass at sunset"></div>
  <h2 class="abs signup-title">Get Email Sign Up</h2>
  <p class="abs signup-copy">Mauris vel lacus vitae felis vestibulum volutpat Etiam est nunc venenatis in tristique eu imperdiet ac nisl Cum sociis natoque penatibus et magnis dis parturient montes</p>
  <div class="abs signup-form"><span class="signup-input">Email address</span><span class="signup-button">Subscribe</span></div>
</section>

<section aria-label="Contact us">
  <h2 class="abs contact-title">Contact Us</h2>
  <span class="abs field-label" style="top:2214px;">Name</span>
  <div class="abs field" style="top:2241px; height:42px;"></div>
  <span class="abs field-label" style="top:2305px;">Email address</span>
  <div class="abs field" style="top:2333px; height:43px;"></div>
  <span class="abs field-label" style="top:2394px;">Message</span>
  <div class="abs field" style="top:2421px; height:95px;"></div>
  <div class="abs submit">SUBMIT</div>
  <div class="abs contact-info">
    412 Meadowlark Lane Suite B20<br>
    Fairhaven, PA 19200<br>
    (555) 014-2738<br>
    hello@willowheart.example
  </div>
  <div class="abs social" aria-label="Social links including chatterloop"><span></span><span></span><span></span><span></span></div>
  <span class="site-name" style="left:690px; top:2510px; font-size:22px;">Willow Heart and Soul</span>
</section>

<footer class="abs site-footer">
  <p class="copyright">© 2017 Company Name&nbsp; All right reserved</p>
  <p class="legal-links">Term of Use |&nbsp; Privacy Policy</p>
</footer>

</body>
</html>
```